New Business Card/Website Logo

We need a business card design for a new company based in Sydney. The company focuses mainly in construction in the field of form work and concreting. Attached is the logo being used already which can be used as a base for a new design, the current one is simply too bland and we are looking to spruce it up so it stands out and looks nicer. The logo would also be used on the website which is currently under construction. The attached image has the name, mobile and also the license number which needs to be there. The current email address on there can be removed and can be replaced with the website http://www.bravelintel.com.au, thanks!
Updates

Target Market(s)

Construction industry. Focusing on form work and concreting

Industry/Entity Type

Construction

Requirements
Must have
• License # on card along with website http://www.bravelintel.com.au and mobile phone number
Nice to have
• You have freedom with the design. The current design was a mock up done quite quickly. Please just keep in mind the target audience - construction, thanks.
Should not have
• the mailvista email address can be removed(refer picture) and replaced somewhere on the design with the website http://www.bravelintel.com.au

```html
<!DOCTYPE html>
<html lang="en">
<head>
<meta charset="utf-8">
<title>Bravelintel Business Card</title>
<link rel="stylesheet" href="https://fonts.googleapis.com/css2?family=Questrial&display=swap">
<style>
  :root {
    --backdrop: #e4e4e2;
    --card: #ffffff;
    --pattern-tone: #ececec;
    --brand-green: #4c9a3e;
    --text-grey: #6d6d6d;
    --badge-text: #ffffff;
  }
  * { box-sizing: border-box; margin: 0; padding: 0; }
  html, body {
    width: 1200px;
    height: 874px;
    overflow: hidden;
    background: var(--backdrop);
  }
  .business-card {
    position: absolute;
    left: 100px;
    top: 151px;
    width: 1000px;
    height: 572px;
    background: var(--card);
    border-radius: 36px;
    box-shadow: 0 6px 24px rgba(0,0,0,0.12);
    overflow: hidden;
    font-family: "Questrial", "Century Gothic", sans-serif;
    color: var(--text-grey);
  }
  .background-texture {
    position: absolute;
    inset: 0;
    background: linear-gradient(160deg, #ffffff 0%, var(--pattern-tone) 55%, #f7f7f7 100%);
    opacity: 0.7;
  }
  .brand-mark {
    position: absolute;
    left: 92px;
    top: 70px;
    display: flex;
    align-items: center;
    gap: 16px;
    color: var(--brand-green);
    font-size: 46px;
    letter-spacing: 4px;
  }
  .brand-mark__square {
    width: 34px;
    height: 34px;
    background: var(--brand-green);
    border-radius: 4px;
  }
  .licence {
    position: absolute;
    right: 70px;
    top: 168px;
    font-size: 30px;
    letter-spacing: 1px;
  }
  .holder-name {
    position: absolute;
    right: 70px;
    top: 318px;
    font-size: 40px;
    color: var(--brand-green);
    letter-spacing: 1px;
  }
  .contact-list {
    position: absolute;
    right: 70px;
    top: 390px;
    list-style: none;
    display: flex;
    flex-direction: column;
    align-items: flex-end;
    gap: 16px;
  }
  .contact-list__item {
    display: flex;
    align-items: center;
    gap: 18px;
    font-size: 27px;
    letter-spacing: 0.5px;
  }
  .contact-list__badge {
    width: 26px;
    height: 26px;
    border-radius: 50%;
    background: var(--brand-green);
    color: var(--badge-text);
    font-size: 13px;
    display: flex;
    align-items: center;
    justify-content: center;
  }
</style>
</head>
<body>
  <div class="business-card">
    <div class="background-texture" role="img" aria-label="Faint repeating block pattern across the card face"></div>

    <div class="brand-mark">
      <span class="brand-mark__square"></span>
      <span class="brand-mark__name">BRAVELINTEL</span>
    </div>

    <p class="licence">Licence: 384512B</p>

    <p class="holder-name">Marco Ellison</p>

    <ul class="contact-list">
      <li class="contact-list__item">
        <span>0412 508 937</span>
        <span class="contact-list__badge">M</span>
      </li>
      <li class="contact-list__item">
        <span>http://www.bravelintel.com.au</span>
        <span class="contact-list__badge">W</span>
      </li>
    </ul>
  </div>
</body>
</html>
```